Professional & Modern Website Design for Quarry Roost Fittings

Our company, a leader in custom furniture and joinery solutions for mining camps, needs a website overhaul. Our current site is looking dated and underwhelming, and we’re seeking a design that truly reflects our professionalism and expertise.

To Whom Are We Speaking?
Our target audience includes asset managers, procurement professionals, and senior-level management from international mining companies. We need a website that speaks directly to these key decision-makers, showcasing our value and expertise.

What We’re Looking For:
Fresh & Modern Aesthetic: We want our website to captivate visitors with a contemporary and sleek design.
Professional Appeal: The new design should convey our commitment to high-quality craftsmanship and service.
Visual Impact: Showcase our custom furniture and joinery work with stunning visuals that highlight our capabilities.
Brochure Alignment: The design should mirror the style and aesthetics of our attached brochure to ensure brand consistency and visual harmony.
Logo & Branding: We want to keep our current logo and branding. The red color should be retained but used sparingly as an accent color to complement the overall design.
Brand Book Usage: Attached is our Brand Book for our Hotel and Accommodation Company. Please use only the correct colors and text from this Brand Book for our Quarry Roost Fittings Brand to ensure consistency and coherence across our branding.
Structured Layout: We require a total of 8 pages, including:
Landing Page: Featuring a prominent contact button
About
Services: Interior Design, Manufacturing, Delivery & Installation
Products: Furniture Packages, Joinery, Upholstery, Beds & Bedding

Our Goals:
Elevate Our Brand: Create a site that mirrors our reputation and industry leadership.
Enhance User Experience: Ensure a seamless, engaging experience for visitors.
Showcase Our Work: Promote our projects and services with impact.

Must include:
Contact us button
Geographical Reach

Previous company website: www.quarryroostfittings.com.au (we wish to convert some of the content from this website to the new platform). Competitor websites that we like: www.dovetelle.com.au,

For functionality we would like it to be designed on Wix.

```html
<!DOCTYPE html>
<html lang="en">
<head>
<meta charset="utf-8">
<title>Quarry Roost Fittings</title>
<link href="https://fonts.googleapis.com/css2?family=Red+Hat+Display:wght@300;400;500;700;800&display=swap" rel="stylesheet">
<style>
:root{
  --red:#d71f2b;
  --ink:#221f20;
  --text:#3a3637;
  --muted:#8a8687;
  --band:#f1f1f1;
  --line:#e2e2e2;
  --white:#ffffff;
  --footer:#221e1f;
}
*{box-sizing:border-box;margin:0;padding:0}
html,body{width:1200px;height:4505px;overflow:hidden}
body{position:relative;font-family:"Red Hat Display",sans-serif;color:var(--text);background:var(--white)}
.abs{position:absolute}
.fill{display:block}

/* header + hero */
.hero{left:0;top:0;width:1200px;height:785px;background:linear-gradient(172deg,#e4e2df 0%,#cbc6c0 9%,#7d6a58 24%,#5a4838 42%,#6f5a47 55%,#9c9187 70%,#6b625a 86%,#4c4540 100%)}
.brand{left:132px;top:24px;display:flex;align-items:center;gap:12px}
.brand-mark{width:44px;height:44px;background:var(--red)}
.brand-name{font-weight:800;font-size:24px;line-height:1.05;color:var(--ink);letter-spacing:1px}
.brand-name span{display:block;font-size:14px;font-weight:500;letter-spacing:.5px}
.nav{left:646px;top:44px;display:flex;gap:22px;font-size:12px;font-weight:500;letter-spacing:.8px;color:var(--ink)}
.btn-contact{left:930px;top:30px;width:134px;height:44px;border:1.5px solid var(--ink);font-size:12px;font-weight:700;letter-spacing:.8px;color:var(--ink);display:flex;align-items:center;justify-content:center}
.hero-arrows{left:1044px;top:702px}

.eyebrow{font-size:18px;font-weight:400;letter-spacing:1px;color:var(--ink);display:flex;align-items:center;gap:14px}
.eyebrow::after{content:"";width:62px;height:3px;background:var(--red)}
.label{font-size:13px;font-weight:700;letter-spacing:1px;color:var(--ink)}
.light{font-weight:300}
.bold{font-weight:800}

.services-band{left:0;top:785px;width:1200px;height:760px;background:linear-gradient(180deg,#f3f3f3 0%,#ffffff 45%)}
.services-title{left:0;top:945px;width:1200px;text-align:center;font-size:40px;line-height:49px;letter-spacing:1.5px;color:var(--ink)}

.card{top:1158px;width:495px;height:271px;border:1px solid var(--line);background:var(--white);display:flex}
.card .photo{width:253px;height:100%;flex:none}
.card .body{padding:70px 0 0 42px}
.card h3{font-size:23px;line-height:27px;letter-spacing:1px;color:var(--ink)}
.link{display:flex;align-items:center;gap:8px;font-size:11px;font-weight:700;letter-spacing:.6px;color:var(--ink);white-space:nowrap}
.link::before{content:"";border-left:9px solid var(--red);border-top:6px solid transparent;border-bottom:6px solid transparent}
.card .link{margin-top:40px}

.intro-band{left:0;top:1544px;width:1200px;height:539px;background:var(--band)}
.intro-title{left:135px;top:1722px;font-size:39px;line-height:45px;letter-spacing:1px;color:var(--ink)}
.intro-copy{left:135px;top:1836px;width:430px;font-size:13.5px;line-height:22.5px;color:var(--text)}

.statement{left:722px;top:2296px;font-size:39px;line-height:45px;letter-spacing:1px;color:var(--ink)}
.statement p{margin-top:18px;font-size:21px;line-height:27px;font-weight:300;letter-spacing:.5px}

.project{top:2714px;width:338px}
.project .photo{height:280px}
.project .link{margin-top:24px}

.geo-title{left:87px;top:3176px;font-size:39px;line-height:45px;letter-spacing:1px;color:var(--ink)}
.geo-copy{left:89px;top:3284px;width:400px;font-size:18px;line-height:26.5px;font-weight:400;letter-spacing:.3px}

.footer{left:0;top:3972px;width:1200px;height:533px;background:var(--footer)}
.form{left:124px;top:3498px;width:451px;height:554px;background:#f2f2f2;padding:32px 46px 0}
.row{display:flex;gap:12px;margin-bottom:18px}
.field{flex:1}
.field label{display:block;font-size:11px;font-weight:700;letter-spacing:.5px;color:var(--ink);margin-bottom:8px}
.field label b{color:var(--red)}
.input{height:38px;background:var(--white);font-size:10px;color:var(--muted);padding:12px 18px}
.textarea{height:74px}
.drop{height:88px;border:1.5px dashed #cfcfcf;background:var(--white);display:flex;align-items:center;justify-content:center;gap:16px;font-size:11px;color:var(--ink);margin-top:22px}
.drop u{color:var(--red)}
.agree{display:flex;align-items:center;gap:8px;font-size:9px;color:var(--text);margin-top:24px}
.agree i{width:15px;height:15px;border:1.5px solid var(--ink);border-radius:2px}
.send{margin-top:24px;height:44px;background:var(--red);color:var(--white);font-size:14px;font-weight:700;letter-spacing:1px;display:flex;align-items:center;justify-content:center;position:relative}
.send svg{position:absolute;right:22px}
.touch{left:659px;top:3612px;font-size:39px;line-height:45px;letter-spacing:1px;color:var(--ink)}
.touch p{margin-top:18px;font-size:18px;line-height:26.5px;font-weight:400;letter-spacing:.3px;color:var(--text)}

.foot-brand{left:87px;top:4206px;display:flex;align-items:center;gap:20px}
.foot-brand .brand-mark{width:64px;height:64px}
.foot-brand .brand-name{color:var(--white);font-size:36px}
.foot-brand .brand-name span{font-size:20px;margin-top:6px}
.foot-col{color:var(--white)}
.foot-col h4{font-size:13px;line-height:19px;font-weight:700;letter-spacing:.5px}
.contact-line{display:flex;gap:14px;margin-top:22px;font-size:12px;line-height:21px;color:#bdb9ba}
.socials{display:flex;gap:10px;margin-top:14px}
.socials i{width:34px;height:34px;border:1px solid #5a5556;border-radius:50%;display:flex;align-items:center;justify-content:center}
.socials i::after{content:"";width:8px;height:8px;background:var(--white);border-radius:50%}
.divider{left:87px;top:4439px;width:1026px;height:1px;background:#4a4546}
.to-top{left:1132px;top:4421px;width:40px;height:40px;border-radius:50%;background:var(--red);display:flex;align-items:center;justify-content:center}
.copyright{left:0;top:4464px;width:1200px;text-align:center;font-size:12px;font-weight:500;color:#d7d3d4;letter-spacing:.3px}
</style>
</head>
<body>

<div class="abs hero fill" role="img" aria-label="Modern living room with wood panelled wall, grey sofa, lounge chairs and forest view windows"></div>
<div class="abs brand"><div class="brand-mark"></div><div class="brand-name">QUARRY ROOST<span>FITTINGS</span></div></div>
<nav class="abs nav"><span>ABOUT</span><span>SERVICES</span><span>PRODUCTS</span></nav>
<div class="abs btn-contact">CONTACT US</div>
<svg class="abs hero-arrows" width="70" height="20" viewBox="0 0 70 20" fill="none" stroke="#ffffff" stroke-width="1.6"><path d="M2 10h22M9 3 2 10l7 7"/><path d="M38 10h28M59 3l7 7-7 7"/></svg>

<div class="abs services-band"></div>
<div class="abs eyebrow" style="left:436px;top:909px">QUARRY ROOST FITTINGS</div>
<h1 class="abs services-title"><span class="light">INTERIOR DESIGN, </span><span class="bold">MANUFACTURING,</span><br><span class="bold">DELIVERY</span><span class="light"> &amp; INSTALLATION</span></h1>

<div class="abs label" style="left:88px;top:1116px">PRODUCTS</div>
<svg class="abs" style="left:1060px;top:1114px" width="52" height="16" viewBox="0 0 52 16" fill="none" stroke-width="1.5"><path d="M2 8h16M7 3 2 8l5 5" stroke="#221f20"/><path d="M28 8h22M45 3l5 5-5 5" stroke="#b5b2b2"/></svg>

<div class="abs card" style="left:89px">
  <div class="photo" role="img" aria-label="Light timber joinery drawer with white cabinet fronts" style="background:linear-gradient(120deg,#d9ad7a 0%,#c48f5a 40%,#e8d6bf 62%,#f4f2ef 80%,#dcd8d2 100%)"></div>
  <div class="body"><h3><span class="light">JOINERY</span><br><span class="bold">FURNITURE</span></h3><div class="link">VIEW PRODUCTS</div></div>
</div>
<div class="abs card" style="left:614px">
  <div class="photo" role="img" aria-label="Upholstery fabric swatches in green, teal and speckled grey" style="background:linear-gradient(125deg,#8fb3a2 0%,#5f8a7a 25%,#1f3a35 48%,#7d7a74 68%,#a8a49c 100%)"></div>
  <div class="body"><h3><span class="light">UPHOLSTERY</span><br><span class="bold">FABRICS</span></h3><div class="link">VIEW PRODUCTS</div></div>
</div>
<div class="abs card" style="left:1140px;width:60px;border-right:none;overflow:hidden">
  <div class="photo" role="img" aria-label="Bed with white bedding" style="width:60px;background:linear-gradient(180deg,#f0eeeb,#cfc8bf 60%,#7e7468)"></div>
</div>

<div class="abs intro-band"></div>
<div class="abs eyebrow" style="left:134px;top:1681px">INTRODUCTION</div>
<h2 class="abs intro-title"><span class="light">WELCOME TO QUARRY</span><br><span class="light">ROOST </span><span class="bold">FITTINGS</span></h2>
<p class="abs intro-copy">Welcome to Quarry Roost Fittings, your trusted partner for custom furniture manufacturing. We specialize in delivering high-quality furniture solutions tailored to your specific needs while ensuring stringent quality control and efficient project management throughout the process.</p>
<div class="abs fill" role="img" aria-label="Dining chair with oatmeal upholstered seat and walnut legs" style="left:673px;top:1600px;width:394px;height:560px;background:linear-gradient(180deg,#cfc6b8 0%,#bdb3a4 50%,#5e3f29 64%,#4a3020 100%)"></div>

<div class="abs fill" role="img" aria-label="Aerial landscape texture in ochre, rust and teal tones" style="left:149px;top:2186px;width:519px;height:388px;background:linear-gradient(125deg,#e09a45 0%,#b4532a 30%,#1f6e70 52%,#c8763a 75%,#8f3b22 100%)"></div>
<div class="abs statement"><span class="light">QUARRY ROOST</span><br><span class="bold">FITTINGS</span><p>IS YOUR ULTIMATE FURNITURE<br>SOLUTIONS PARTNER.</p></div>

<div class="abs label" style="left:86px;top:2669px">OUR PROJECTS</div>
<svg class="abs" style="left:1058px;top:2667px" width="52" height="16" viewBox="0 0 52 16" fill="none" stroke-width="1.5"><path d="M2 8h16M7 3 2 8l5 5" stroke="#221f20"/><path d="M28 8h22M45 3l5 5-5 5" stroke="#b5b2b2"/></svg>
<div class="abs project" style="left:89px"><div class="photo" role="img" aria-label="Hotel bedroom with olive bed runner and timber bed frame" style="background:linear-gradient(180deg,#f2f1ee 0%,#dedad3 45%,#4f5a35 60%,#a3835f 72%,#4a4744 100%)"></div><div class="link">VIEW PROJECT</div></div>
<div class="abs project" style="left:446px"><div class="photo" role="img" aria-label="White bedding against timber headboard with reading light" style="background:linear-gradient(110deg,#fbfaf8 0%,#e9e6e1 40%,#c48f5f 62%,#a9764b 78%,#e39a78 100%)"></div><div class="link">VIEW PROJECT</div></div>
<div class="abs project" style="left:801px"><div class="photo" role="img" aria-label="Timber wardrobe, desk and wall-mounted television in a room" style="background:linear-gradient(90deg,#5a4232 0%,#8a6b52 30%,#ecebe8 50%,#dcdbd7 80%,#5d6a3a 100%)"></div><div class="link">VIEW PROJECT</div></div>
<div class="abs project" style="left:1158px;width:42px;overflow:hidden"><div class="photo" role="img" aria-label="Timber room interior" style="background:linear-gradient(180deg,#c49c76,#e6dccf)"></div><div class="link">VIEW</div></div>

<h2 class="abs geo-title"><span class="light">GEOGRAPHICAL</span><br><span class="bold">REACH</span></h2>
<p class="abs geo-copy">WITH A GLOBAL PRESENCE, OUR SERVICES EXTEND TO AUSTRALIA, NEW ZEALAND,SOUTH EAST ASIA, AND THE UNITED ARAB EMIRATES.</p>
<div class="abs fill" role="img" aria-label="World map in light grey with Asia-Pacific and the Middle East highlighted in gold" style="left:537px;top:3143px;width:561px;height:276px;background:linear-gradient(90deg,#f1f1f1 0%,#e6e6e6 40%,#d4b47a 62%,#c49a52 80%,#ececec 100%)"></div>

<div class="abs footer"></div>
<form class="abs form">
  <div class="row"><div class="field"><label>NAME<b>*</b></label><div class="input">Enter your name</div></div><div class="field"><label>PHONE<b>*</b></label><div class="input">Enter phone number</div></div></div>
  <div class="row"><div class="field"><label>EMAIL<b>*</b></label><div class="input">Enter your email</div></div><div class="field"><label>ADDRESS<b>*</b></label><div class="input">Enter your address</div></div></div>
  <div class="field"><label>MESSAGE<b>*</b></label><div class="input textarea">Enter your message</div></div>
  <div class="drop"><svg width="18" height="18" viewBox="0 0 18 18" fill="none" stroke="#221f20" stroke-width="1.5"><path d="M9 12V2M5 6l4-4 4 4M2 11v5h14v-5"/></svg><span><u>Choose file</u> or drop here</span></div>
  <div class="agree"><i></i>I agree to the terms and conditions.</div>
  <div class="send">SEND MESSAGE<svg width="18" height="16" viewBox="0 0 18 16" fill="#ffffff"><path d="M1 8 17 1l-4 14-4-5-3 3V9l9-6-10 6z"/></svg></div>
</form>
<h2 class="abs touch"><span class="light">GET IN TOUCH</span><br><span class="bold">WITH US</span><p>LET'S GET THIS CONVERSATION STARTED.<br>TELL US A BIT ABOUT YOURSELF, AND WE'LL<br>GET IN TOUCH AS SOON AS WE CAN.</p></h2>

<div class="abs foot-brand"><div class="brand-mark"></div><div class="brand-name">QUARRY ROOST<span>FITTINGS</span></div></div>

<div class="abs foot-col" style="left:539px;top:4156px;width:230px">
  <h4>IF YOU HAVE ANY QUESTIONS,<br>LET US KNOW</h4>
  <div class="contact-line" style="margin-top:16px"><svg width="14" height="14" viewBox="0 0 14 14" fill="#d71f2b"><path d="M3 1l2 3-1.5 1.5a8 8 0 0 0 5 5L10 9l3 2-1 2.5C6 13 1 8 .5 2z"/></svg><span>Phone:<br>1300 555 014</span></div>
  <div style="height:1px;background:#4a4546;margin-top:12px"></div>
  <h4 style="margin-top:22px">FOLLOW US</h4>
  <div class="socials"><i></i><i></i></div>
</div>
<div class="abs foot-col" style="left:836px;top:4156px;width:290px">
  <h4>GET IN TOUCH<br>WITH US</h4>
  <div class="contact-line" style="margin-top:16px"><svg width="14" height="14" viewBox="0 0 14 14" fill="#d71f2b"><path d="M3 1l2 3-1.5 1.5a8 8 0 0 0 5 5L10 9l3 2-1 2.5C6 13 1 8 .5 2z"/></svg><span>Mobile:<br>+61 400 555 127</span></div>
  <div class="contact-line"><svg width="14" height="12" viewBox="0 0 14 12" fill="#d71f2b"><path d="M0 0h14v12H0z"/><path d="M0 0l7 6 7-6" stroke="#221e1f" stroke-width="1.4" fill="none"/></svg><span>Email:<br>alex@quarryroostfittings.com.au<br>hello@quarryroostfittings.com.au</span></div>
</div>

<div class="abs divider"></div>
<div class="abs to-top"><svg width="10" height="6" viewBox="0 0 10 6" fill="none" stroke="#ffffff" stroke-width="1.6"><path d="M1 5l4-4 4 4"/></svg></div>
<div class="abs copyright">© COPYRIGHT 2024 QUARRY ROOST FITTINGS, ALL RIGHTS RESERVED</div>

</body>
</html>
```